Tarn Ridge Edibles product label

We are looking to create a product label for a new product. We are a THC edible company. Labels must not contain anything that resembles marijuana. Labels also must not contain anything that is appealing to children. The state is very strict. I want a professional label but also fun.

What the label must include.
Logo/Name (I will provide that in a file)
Dose: 50mg per pack
Servings: 10 servings per pack
Warning label for kids
Assorted flavors

Please be creative. Label size will need to be 3" wide and 5" tall.

```html
<!DOCTYPE html>
<html lang="en">
<head>
<meta charset="UTF-8">
<title>Tarn Ridge Edibles – Product Label</title>
<link href="https://fonts.googleapis.com/css2?family=Montserrat:wght@400;500;600&display=swap" rel="stylesheet">
<style>
  :root {
    --stage: #d9dcdc;
    --label-white: #ffffff;
    --panel-grey: #5a5a5a;
    --brand-green: #6f9a3a;
    --text-light: #f4f4f4;
    --warn-red: #e3131b;
    --warn-yellow: #f5c400;
    --ink: #111111;
  }
  * { box-sizing: border-box; margin: 0; padding: 0; }
  html, body {
    width: 1200px; height: 884px; overflow: hidden;
    background: var(--stage);
    font-family: "Montserrat", sans-serif;
  }
  .canvas {
    width: 1200px; height: 884px;
    display: flex; align-items: center; justify-content: center;
  }
  .label {
    width: 492px; height: 820px;
    background: var(--label-white);
    display: flex; flex-direction: column;
  }
  .brand-area {
    height: 440px;
    display: flex; align-items: center; justify-content: center; gap: 22px;
    padding: 0 30px;
  }
  .brand-mark {
    flex: none;
    width: 64px; height: 64px; background: var(--brand-green);
  }
  .brand-name {
    color: var(--brand-green);
    font-weight: 600; font-size: 50px; line-height: 1.1;
  }
  .info-panel {
    height: 358px;
    background: var(--panel-grey);
    position: relative;
  }
  .facts {
    position: absolute; left: 18px; top: 44px;
    color: var(--text-light);
    font-size: 29px; font-weight: 400; line-height: 36px;
    list-style: none;
    white-space: nowrap;
  }
  .warning-box {
    position: absolute; left: 21px; top: 192px;
    width: 451px; height: 119px;
    background: var(--label-white);
    border: 4px solid var(--ink);
    display: flex; align-items: center; padding-left: 14px; gap: 12px;
  }
  .warning-icons { display: flex; gap: 12px; align-items: center; }
  .warning-text { flex: 1; text-align: center; }
  .warning-title {
    color: var(--warn-red); font-size: 40px; font-weight: 500; line-height: 1;
  }
  .warning-sub {
    color: var(--ink); font-size: 26px; font-weight: 500; line-height: 1.15;
  }
  .bottom-strip { flex: 1; background: var(--label-white); }
</style>
</head>
<body>
<main class="canvas">
  <section class="label">
    <header class="brand-area">
      <span class="brand-mark"></span>
      <span class="brand-name">Tarn Ridge<br>Edibles</span>
    </header>
    <div class="info-panel">
      <ul class="facts">
        <li>Dosage: 50mg per pack</li>
        <li>Servings: 10 servings per pack</li>
        <li>Smell: Assorted flavors</li>
      </ul>
      <div class="warning-box">
        <div class="warning-icons">
          <svg width="68" height="68" viewBox="0 0 72 72" aria-label="Not for children sign">
            <circle cx="36" cy="36" r="32" fill="none" stroke="var(--warn-red)" stroke-width="5"/>
            <line x1="13" y1="13" x2="59" y2="59" stroke="var(--warn-red)" stroke-width="5"/>
          </svg>
          <svg width="76" height="68" viewBox="0 0 80 72" aria-label="Caution sign">
            <polygon points="40,4 76,68 4,68" fill="var(--warn-yellow)" stroke="var(--ink)" stroke-width="3" stroke-linejoin="round"/>
            <rect x="37" y="24" width="6" height="28" rx="2" fill="var(--ink)"/>
            <circle cx="40" cy="59" r="3.5" fill="var(--ink)"/>
          </svg>
        </div>
        <div class="warning-text">
          <div class="warning-title">WARNING</div>
          <div class="warning-sub">Not for children</div>
        </div>
      </div>
    </div>
    <div class="bottom-strip"></div>
  </section>
</main>
</body>
</html>
```